Change of trading name, rebrand

existing website to be updated with new theme and logo. existing website is
www.brambleworth.com.au
Industry/Entity Type
Construction
Coding
Coded - Design and coding required
Number of Pages Required
5+ page
Requirements
Must have
- be mobile phone friendly

```html
<!DOCTYPE html>
<html lang="en">
<head>
<meta charset="utf-8">
<meta name="viewport" content="width=1200">
<title>Brambleworth Plant Hire</title>
<link href="https://fonts.googleapis.com/css2?family=Archivo:wght@400;500;600;700;800;900&family=Poppins:wght@400;500;600&family=Racing+Sans+One&display=swap" rel="stylesheet">
<style>
:root{
  --navy:#28299a;
  --blue:#3338c9;
  --ink:#141414;
  --dark:#1a1a1a;
  --grey:#d8d8d8;
  --light:#f3f3f3;
  --white:#ffffff;
  --text:#333333;
}
*{box-sizing:border-box;margin:0;padding:0}
html,body{width:1200px;height:5259px;overflow:hidden}
body{position:relative;background:var(--white);font-family:"Poppins",sans-serif;color:var(--text)}
.abs{position:absolute}
.display{font-family:"Racing Sans One",sans-serif;color:var(--navy);letter-spacing:2px;text-transform:uppercase;font-weight:400;line-height:1;white-space:nowrap}
.btn{position:absolute;display:flex;align-items:center;justify-content:center;font-family:"Archivo",sans-serif;font-size:10px;font-weight:600;text-transform:uppercase;color:var(--white);background:var(--navy);border:2px solid var(--white);box-shadow:0 0 0 2px var(--navy);letter-spacing:.3px}
.btn.dark{background:var(--ink);box-shadow:0 0 0 2px var(--ink)}
.center{text-align:center;left:0;width:1200px}

/* header */
.header{top:0;left:0;width:1200px;height:71px;background:var(--white)}
.nav{top:71px;left:0;width:1200px;height:32px;background:var(--ink)}
.nav-item{position:absolute;top:0;height:32px;display:flex;align-items:center;color:var(--white);font-family:"Archivo",sans-serif;font-size:10.5px;font-weight:500;text-transform:uppercase}
.nav-item.active{background:var(--blue);justify-content:center;width:90px}
.logo-tab{top:0;left:126px;width:200px;height:124px}
.brand{position:absolute;font-family:"Archivo",sans-serif;font-weight:900;color:var(--navy);text-transform:uppercase;text-align:center;line-height:1.05}
.call-icon{top:16px;left:735px;width:36px;height:36px;background:var(--navy);display:flex;align-items:center;justify-content:center}
.call-label{top:19px;left:786px;font-family:"Archivo",sans-serif;font-size:9px;font-weight:600;color:var(--blue)}
.call-number{top:30px;left:786px;font-family:"Archivo",sans-serif;font-size:18px;font-weight:700;color:var(--ink)}

/* hero */
.hero{top:103px;left:0;width:1200px;height:600px;background:linear-gradient(100deg,#ececee 0%,#e3e3e6 55%,#d8d8dc 100%)}
.hero-photo{top:30px;left:600px;width:600px;height:510px;background:radial-gradient(ellipse at 55% 55%,#e2ad2a 0%,#c9962b 30%,rgba(170,165,150,.5) 60%,rgba(220,220,224,0) 78%)}
.hero-kicker{top:234px;left:140px;font-family:"Archivo",sans-serif;font-size:21px;font-weight:600;color:var(--ink);line-height:26px}
.hero-title{top:268px;left:138px;font-size:54px;line-height:56px}
.hero-sub{top:386px;left:141px;font-family:"Archivo",sans-serif;font-size:12.5px;font-weight:700;color:var(--ink);line-height:22px;text-transform:uppercase}

/* about */
.about-frame{top:755px;left:194px;width:404px;height:428px}
.about-photo{top:755px;left:194px;width:384px;height:416px;background:linear-gradient(160deg,#c9b35a 0%,#b9c3cf 45%,#8ea1b5 100%);clip-path:polygon(0 0,88% 0,100% 8%,100% 100%,8% 100%,0 94%)}
.about-title{top:778px;left:643px;font-size:50px}
.about-lead{top:846px;left:643px;width:380px;font-family:"Archivo",sans-serif;font-size:12.5px;font-weight:700;color:var(--ink);line-height:21px;text-transform:uppercase}
.about-copy{left:643px;width:370px;font-size:10.6px;line-height:20.5px;color:#444}

/* featured */
.featured-bg{top:1250px;left:0;width:1200px;height:1040px}
.section-title-light{color:var(--white)}
.sub-light{color:var(--white);font-family:"Archivo",sans-serif;font-size:12px;font-weight:500;line-height:21px;text-transform:uppercase}
.equip-card{position:absolute;top:1618px;width:243px;height:344px;background:var(--white);padding:6px}
.equip-photo{width:100%;height:278px}
.equip-label{position:absolute;left:0;bottom:10px;width:100%;text-align:center;font-family:"Archivo",sans-serif;font-size:24px;font-weight:800;letter-spacing:1.5px;color:var(--navy);text-transform:uppercase}
.equip-card.mid .equip-photo{height:332px}
.equip-card.mid .equip-label{color:var(--white);bottom:14px}
.arrow{position:absolute;width:40px;height:38px;background:#f1f1f1;display:flex;align-items:center;justify-content:center}
.dots{top:1993px;left:553px;display:flex;gap:4px}
.dots span{width:16px;height:3px;background:#888}
.dots span.on{background:var(--blue)}

/* services */
.sub-dark{font-family:"Archivo",sans-serif;font-size:12px;font-weight:600;color:var(--ink);line-height:21px;text-transform:uppercase}
.service-card{position:absolute;top:2454px;width:246px;height:338px;background:var(--light);border:1px solid #e2e2e2;padding:9px;text-align:center}
.service-photo{width:100%;height:180px}
.service-name{margin-top:22px;font-family:"Archivo",sans-serif;font-size:16.5px;font-weight:600;color:var(--navy);text-transform:uppercase;letter-spacing:.3px}
.service-copy{margin:10px auto 0;width:210px;font-size:10px;line-height:19px;color:#444}
.service-btn{margin:10px auto 0;width:118px;height:30px;background:var(--ink);color:var(--white);font-family:"Archivo",sans-serif;font-size:9px;font-weight:600;display:flex;align-items:center;justify-content:center;text-transform:uppercase;border:2px solid var(--white);box-shadow:0 0 0 1px var(--ink)}
.service-card.featured{background:var(--navy);border-color:var(--navy)}
.service-card.featured .service-name,.service-card.featured .service-copy{color:var(--white)}
.service-card.featured .service-btn{background:var(--white);color:var(--ink);box-shadow:0 0 0 1px var(--white);border-color:var(--navy)}

/* why */
.why-bg{top:2850px;left:0;width:1200px;height:800px}
.why-box{position:absolute;top:3199px;width:162px;height:158px;background:var(--white);display:flex;align-items:center;justify-content:center;border:1px solid #e6e6e6}
.why-box.on{background:var(--navy);border:6px solid var(--white)}
.why-label{position:absolute;top:3378px;width:190px;text-align:center;font-family:"Archivo",sans-serif;font-size:13px;font-weight:600;color:var(--ink);line-height:19px;text-transform:uppercase}

/* projects */
.project-card{position:absolute;top:3825px;width:243px;height:242px}
.project-card.mid{border:6px solid var(--navy)}
.project-caption{position:absolute;left:0;bottom:14px;width:100%;text-align:center;font-family:"Archivo",sans-serif;font-size:13px;font-weight:600;color:var(--white);line-height:19px;text-transform:uppercase}

/* contact */
.contact-label{font-family:"Archivo",sans-serif;font-size:10px;font-weight:700;color:var(--blue);text-transform:uppercase}
.contact-value{font-family:"Archivo",sans-serif;font-size:11.5px;font-weight:500;color:var(--ink)}
.quote{top:4247px;left:551px;width:414px;height:432px;border:3px solid var(--navy);background:var(--white)}
.quote-title{position:absolute;top:38px;left:0;width:100%;text-align:center;font-family:"Archivo",sans-serif;font-size:32px;font-weight:800;color:var(--ink);text-transform:uppercase}
.quote-sub{position:absolute;top:98px;left:0;width:100%;text-align:center;font-family:"Archivo",sans-serif;font-size:10.5px;font-weight:600;color:var(--ink);line-height:19px;text-transform:uppercase}
.field{position:absolute;height:38px;border:1px solid #e1e1e1;background:#fbfbfb;padding:10px 14px;font-size:8px;color:#888;text-transform:uppercase}
.truck-photo{top:4627px;left:0;width:337px;height:270px;background:radial-gradient(ellipse at 45% 55%,#e3a72a 0%,#c88f1e 35%,#3a3a3a 60%,rgba(255,255,255,0) 75%)}

/* footer */
.footer-bg{top:4740px;left:0;width:1200px;height:519px}
.foot-head{font-family:"Archivo",sans-serif;font-size:14px;font-weight:600;color:var(--white);text-transform:uppercase}
.foot-links{font-family:"Archivo",sans-serif;font-size:9.5px;color:var(--white);line-height:27.5px;text-transform:uppercase}
.foot-small{font-family:"Archivo",sans-serif;font-size:9.5px;color:var(--white);text-transform:uppercase}
.social{position:absolute;top:5032px;width:30px;height:30px;border:1px solid var(--white)}
.social.on{background:var(--blue);border-color:var(--blue)}
.copyright{top:5225px;font-family:"Archivo",sans-serif;font-size:9px;color:#cfcfcf;text-transform:uppercase}
</style>
</head>
<body>

<!-- HEADER -->
<header class="abs header"></header>
<nav class="abs nav">
  <div class="nav-item active" style="left:380px">Home</div>
  <div class="nav-item" style="left:500px">About Us</div>
  <div class="nav-item" style="left:612px">Plant Hire &nbsp;<svg width="9" height="6" viewBox="0 0 9 6"><path d="M1 1l3.5 3.5L8 1" stroke="#fff" stroke-width="1.4" fill="none"/></svg></div>
  <div class="nav-item" style="left:754px">Project Snapshot</div>
  <div class="nav-item" style="left:922px">Policies</div>
  <div class="nav-item" style="left:1030px">Jobs</div>
</nav>
<svg class="abs logo-tab" viewBox="0 0 200 124"><polygon points="0,0 200,0 200,100 182,124 18,124 0,100" fill="#fff"/></svg>
<div class="brand" style="top:50px;left:126px;width:200px;font-size:19px">Brambleworth<br>Plant Hire</div>

<div class="abs call-icon"><svg width="18" height="18" viewBox="0 0 24 24"><path d="M6.6 10.8a15.1 15.1 0 006.6 6.6l2.2-2.2c.3-.3.7-.4 1-.2 1.1.4 2.3.6 3.6.6.6 0 1 .4 1 1V20c0 .6-.4 1-1 1A17 17 0 013 4c0-.6.4-1 1-1h3.5c.6 0 1 .4 1 1 0 1.3.2 2.5.6 3.6.1.3 0 .7-.2 1z" fill="#fff"/></svg></div>
<div class="abs call-label">CALL US TODAY!</div>
<div class="abs call-number">1300 555 014</div>
<div class="btn" style="top:16px;left:934px;width:123px;height:37px">Contact Us</div>

<!-- HERO -->
<section class="abs hero">
  <div class="abs hero-photo" role="img" aria-label="Yellow tracked excavator with a site worker in a hard hat behind it"></div>
</section>
<div class="abs hero-kicker">COMMITTED TO SUPERIOR QUALITY</div>
<h1 class="abs display hero-title">Plant Hire<br>Services</h1>
<p class="abs hero-sub">Specialise in the hire of heavy earthmoving, mining<br>and construction machines.</p>
<div class="btn" style="top:458px;left:141px;width:179px;height:45px">Request a Quote</div>
<svg class="abs" style="top:520px;left:0" width="1200" height="190" viewBox="0 0 1200 190">
  <polygon points="0,136 1200,40 1200,190 0,190" fill="#fff"/>
  <polygon points="0,135 0,165 560,86" fill="#3338c9"/>
</svg>

<!-- ABOUT -->
<svg class="abs about-frame" viewBox="0 0 404 428"><polyline points="342,2 402,62 402,426 18,426" fill="none" stroke="#141414" stroke-width="2.5"/></svg>
<div class="abs about-photo" role="img" aria-label="Smiling site manager in a blue hard hat with arms crossed beside machinery"></div>
<h2 class="abs display about-title">About Us</h2>
<p class="abs about-lead">Welcome to BWR Heavy Equipment Hire. Company that was established in 2010.</p>
<p class="abs about-copy" style="top:893px">Brambleworth Heavy Equipment Hire specialise in the hire of heavy earthmoving, mining and construction machines with specialised attachments and tooling. Our array of machines &amp; attachments is second to none and we have one of the largest hire fleets available in South East Queensland. If its plant hire you require, then Brambleworth Resources, BWR as the local's call us should be the first call you make.</p>
<p class="abs about-copy" style="top:1047px">we provide excellent operators &amp; quality machines across all makes &amp; models to guarantee you maximum up-time.</p>
<div class="btn" style="top:1114px;left:645px;width:122px;height:40px">Learn More</div>
<div class="btn dark" style="top:1114px;left:779px;width:122px;height:40px">Contact Us</div>

<!-- FEATURED EQUIPMENT -->
<svg class="abs featured-bg" viewBox="0 0 1200 1040">
  <polygon points="0,148 1200,20 1200,790 0,990" fill="#181818"/>
  <polygon points="640,72 1200,0 1200,26" fill="#3338c9"/>
  <polygon points="0,990 0,1025 590,930" fill="#3338c9"/>
</svg>
<h2 class="abs display center section-title-light" style="top:1460px;font-size:50px">Featured Equipment</h2>
<p class="abs center sub-light" style="top:1524px">Reliable plant hire spanning Queensland &amp; surrounds.<br>We have one of the largest &amp; most versatile fleets in South East Queensland.</p>
<div class="arrow" style="top:1770px;left:122px"><svg width="10" height="12" viewBox="0 0 10 12"><path d="M7 1L2 6l5 5" stroke="#222" stroke-width="1.6" fill="none"/></svg></div>
<div class="arrow" style="top:1770px;left:1036px"><svg width="10" height="12" viewBox="0 0 10 12"><path d="M3 1l5 5-5 5" stroke="#222" stroke-width="1.6" fill="none"/></svg></div>
<div class="equip-card" style="left:203px"><div class="equip-photo" role="img" aria-label="Yellow backhoe loader parked under a blue sky" style="background:linear-gradient(180deg,#4d79b8 0%,#8fb0d6 45%,#d6a62b 70%,#5c5a55 100%)"></div><div class="equip-label">Backhoes</div></div>
<div class="equip-card mid" style="left:476px"><div class="equip-photo" role="img" aria-label="Articulated dump truck on a gravel stockpile under cloudy sky" style="background:linear-gradient(180deg,#3d6fb0 0%,#b7c8dc 40%,#b99a5a 65%,#3b3225 100%)"></div><div class="equip-label">Bobcats</div></div>
<div class="equip-card" style="left:750px"><div class="equip-photo" role="img" aria-label="Yellow soil compactor roller on a dirt site" style="background:linear-gradient(180deg,#6f9ed2 0%,#a9c5e2 40%,#d9a52f 65%,#8b7a63 100%)"></div><div class="equip-label">Compactor</div></div>
<div class="abs dots"><span></span><span class="on"></span><span></span><span></span><span></span></div>
<div class="btn" style="top:2040px;left:506px;width:188px;height:41px">Explore Our Equipment</div>

<!-- SERVICES -->
<h2 class="abs display center" style="top:2303px;font-size:50px">Services</h2>
<p class="abs center sub-dark" style="top:2366px">The service provided by Brambleworth is guaranteed<br>to be an unparalleled experience.</p>
<div class="service-card" style="left:206px"><div class="service-photo" role="img" aria-label="Row of yellow loaders and excavators lined up on a yard" style="background:linear-gradient(180deg,#b9c7d6 0%,#c7a255 55%,#b48b58 100%)"></div><div class="service-name">Equipment Rental</div><p class="service-copy">We provide a wide selection of heavy equipment for hire</p><div class="service-btn">Learn More</div></div>
<div class="service-card featured" style="left:477px"><div class="service-photo" role="img" aria-label="Technician servicing a large orange machine" style="background:linear-gradient(135deg,#c9851f 0%,#e0a23a 50%,#6b4a20 100%)"></div><div class="service-name">Maintenance &amp; Repair</div><p class="service-copy">Our experienced technicians offer maintenance and repair services</p><div class="service-btn">Learn More</div></div>
<div class="service-card" style="left:751px"><div class="service-photo" role="img" aria-label="Worker in a hard hat operating equipment controls on site" style="background:linear-gradient(135deg,#8da0b6 0%,#d6a13a 55%,#9b7a4f 100%)"></div><div class="service-name">On-Site Support</div><p class="service-copy">Our team can provide onsite assistance to ensure your equipment operated.</p><div class="service-btn">Learn More</div></div>

<!-- WHY CHOOSE -->
<svg class="abs why-bg" viewBox="0 0 1200 800">
  <polygon points="0,150 1200,20 1200,640 0,800" fill="#d6d6d6"/>
  <polygon points="660,95 1200,14 1200,36" fill="#3338c9"/>
</svg>
<h2 class="abs display center" style="top:3048px;font-size:50px">Why Choose BWR</h2>
<p class="abs center sub-dark" style="top:3111px">The service provided by Brambleworth is guaranteed<br>to be an unparalleled experience.</p>

<div class="why-box" style="left:141px"><svg width="76" height="68" viewBox="0 0 76 68"><circle cx="22" cy="14" r="10" fill="#28299a"/><rect x="6" y="28" width="32" height="36" rx="8" fill="#28299a"/><rect x="42" y="34" width="22" height="28" rx="4" fill="#28299a"/><path d="M58 4l3 7 7 3-7 3-3 7-3-7-7-3 7-3z" fill="#28299a"/></svg></div>
<div class="why-box on" style="left:331px"><svg width="84" height="64" viewBox="0 0 84 64"><path d="M10 10h46l8 16h14v18H6z" fill="none" stroke="#fff" stroke-width="5" stroke-linejoin="round"/><circle cx="22" cy="48" r="10" fill="#28299a" stroke="#fff" stroke-width="5"/><circle cx="62" cy="48" r="10" fill="#28299a" stroke="#fff" stroke-width="5"/></svg></div>
<div class="why-box" style="left:520px"><svg width="60" height="68" viewBox="0 0 60 68"><path d="M30 4l24 10v20c0 16-11 26-24 30C17 60 6 50 6 34V14z" fill="#28299a"/></svg></div>
<div class="why-box" style="left:708px"><svg width="72" height="72" viewBox="0 0 72 72"><circle cx="30" cy="38" r="20" fill="none" stroke="#28299a" stroke-width="12" stroke-dasharray="9 6"/><circle cx="30" cy="38" r="7" fill="#fff"/><rect x="52" y="6" width="10" height="60" rx="4" fill="#28299a"/></svg></div>
<div class="why-box" style="left:898px"><svg width="80" height="70" viewBox="0 0 80 70"><rect x="4" y="52" width="72" height="14" rx="7" fill="#28299a"/><rect x="10" y="32" width="30" height="16" fill="#28299a"/><path d="M40 36L58 10l12 10" fill="none" stroke="#28299a" stroke-width="6"/><rect x="64" y="18" width="10" height="14" fill="#28299a"/></svg></div>

<div class="why-label" style="left:127px">20+ Years<br>of Experience</div>
<div class="why-label" style="left:317px">100 +<br>Machines in Fleet</div>
<div class="why-label" style="left:506px">One of QLD's<br>largest suppliers</div>
<div class="why-label" style="left:694px">Onsite Servicing</div>
<div class="why-label" style="left:884px">Custom Machine<br>Attachments</div>
<div class="btn" style="top:3448px;left:523px;width:155px;height:40px">Request a Quote</div>

<svg class="abs" style="top:3600px;left:0" width="1200" height="80" viewBox="0 0 1200 80"><polygon points="0,60 0,82 560,10" fill="#3338c9"/></svg>

<!-- PROJECTS -->
<h2 class="abs display center" style="top:3690px;font-size:50px">Projects</h2>
<p class="abs center sub-dark" style="top:3757px">We're incredibly proud of our major project experience.</p>
<div class="arrow" style="top:3928px;left:122px"><svg width="10" height="12" viewBox="0 0 10 12"><path d="M7 1L2 6l5 5" stroke="#222" stroke-width="1.6" fill="none"/></svg></div>
<div class="arrow" style="top:3928px;left:1036px"><svg width="10" height="12" viewBox="0 0 10 12"><path d="M3 1l5 5-5 5" stroke="#222" stroke-width="1.6" fill="none"/></svg></div>
<div class="project-card" style="left:207px" role="img" aria-label="Orange excavator loading dirt on a bush site"><div style="width:100%;height:100%;background:linear-gradient(180deg,#6f8a5a 0%,#d0702a 45%,#8a7a66 100%)"></div></div>
<div class="project-card mid" style="left:476px"><div style="width:100%;height:100%;background:linear-gradient(180deg,#6f9ac6 0%,#9fb7a0 40%,#c9a23a 62%,#3a3428 100%)" role="img" aria-label="Bulldozer clearing ground on a road upgrade site"></div><div class="project-caption">Riverside Upgrade<br>Project (RUP) Brisbane</div></div>
<div class="project-card" style="left:750px" role="img" aria-label="Yellow excavator on a sandy site under blue sky"><div style="width:100%;height:100%;background:linear-gradient(180deg,#2f63b8 0%,#6f9cd6 45%,#d6a934 65%,#a79a84 100%)"></div></div>
<div class="btn" style="top:4107px;left:508px;width:182px;height:41px">See More Projects</div>

<!-- CONTACT -->
<div class="brand" style="top:4300px;left:215px;width:180px;font-size:19px">Brambleworth<br>Plant Hire</div>
<div class="abs contact-label" style="top:4421px;left:235px">Head Office:</div>
<div class="abs contact-value" style="top:4436px;left:235px;font-size:10.5px">18 WATTLEBANK RD, COOMERA QLD 4209</div>
<div class="abs call-icon" style="top:4485px;left:235px"><svg width="18" height="18" viewBox="0 0 24 24"><path d="M6.6 10.8a15.1 15.1 0 006.6 6.6l2.2-2.2c.3-.3.7-.4 1-.2 1.1.4 2.3.6 3.6.6.6 0 1 .4 1 1V20c0 .6-.4 1-1 1A17 17 0 013 4c0-.6.4-1 1-1h3.5c.6 0 1 .4 1 1 0 1.3.2 2.5.6 3.6.1.3 0 .7-.2 1z" fill="#fff"/></svg></div>
<div class="abs contact-label" style="top:4488px;left:288px;color:var(--ink)">Call Us</div>
<div class="abs contact-value" style="top:4500px;left:288px;font-size:19px;font-weight:600">1300 555 014</div>
<div class="abs contact-label" style="top:4557px;left:235px">Email:</div>
<div class="abs contact-value" style="top:4572px;left:235px">hire@brambleworth.com.au</div>

<div class="abs quote">
  <div class="quote-title">Request a Quote</div>
  <div class="quote-sub">Send us your project details<br>and we will reply within one day</div>
  <div class="field" style="top:152px;left:26px;width:178px">First Name</div>
  <div class="field" style="top:152px;left:210px;width:178px">Last Name</div>
  <div class="field" style="top:198px;left:26px;width:178px">Email</div>
  <div class="field" style="top:198px;left:210px;width:178px">Phone Number</div>
  <div class="field" style="top:244px;left:26px;width:362px;height:102px">Message</div>
  <div class="btn" style="top:364px;left:130px;width:154px;height:36px;font-size:10px">Submit Now</div>
</div>
<div class="abs truck-photo" role="img" aria-label="Large yellow mining dump truck"></div>

<!-- FOOTER -->
<svg class="abs footer-bg" viewBox="0 0 1200 519">
  <polygon points="0,170 1200,60 1200,519 0,519" fill="#181818"/>
  <polygon points="660,100 1200,22 1200,44" fill="#3338c9"/>
</svg>
<div class="brand" style="top:4985px;left:140px;width:180px;font-size:19px;color:var(--white)">Brambleworth<br>Plant Hire</div>
<div class="social" style="left:152px"></div>
<div class="social on" style="left:191px"></div>
<div class="social" style="left:230px"></div>
<div class="social" style="left:269px"></div>

<div class="abs foot-head" style="top:4955px;left:384px">Quick Links</div>
<div class="abs foot-links" style="top:4990px;left:384px">Home<br>About Us<br>Machine Operator Jobs<br>Plant Hire<br>Attachments Hire<br>Policies</div>

<div class="abs foot-head" style="top:4955px;left:608px">Contact Us</div>
<svg class="abs" style="top:4998px;left:603px" width="18" height="22" viewBox="0 0 18 22"><path d="M9 1a7 7 0 017 7c0 5-7 13-7 13S2 13 2 8a7 7 0 017-7z" fill="none" stroke="#fff" stroke-width="1.6"/><circle cx="9" cy="8" r="2.5" fill="none" stroke="#fff" stroke-width="1.6"/></svg>
<div class="abs foot-small" style="top:4993px;left:637px;color:#5d62e6">Head Office:</div>
<div class="abs foot-small" style="top:5006px;left:637px;line-height:14px">18 Wattlebank Rd,<br>Coomera QLD 4209</div>
<svg class="abs" style="top:5061px;left:603px" width="18" height="18" viewBox="0 0 24 24"><path d="M6.6 10.8a15.1 15.1 0 006.6 6.6l2.2-2.2c.3-.3.7-.4 1-.2 1.1.4 2.3.6 3.6.6.6 0 1 .4 1 1V20c0 .6-.4 1-1 1A17 17 0 013 4c0-.6.4-1 1-1h3.5c.6 0 1 .4 1 1 0 1.3.2 2.5.6 3.6.1.3 0 .7-.2 1z" fill="none" stroke="#fff" stroke-width="1.6"/></svg>
<div class="abs foot-small" style="top:5056px;left:637px;color:#5d62e6">Call Us</div>
<div class="abs" style="top:5069px;left:637px;font-family:'Archivo',sans-serif;font-size:16px;font-weight:600;color:#fff">1300 555 014</div>
<svg class="abs" style="top:5115px;left:603px" width="20" height="15" viewBox="0 0 20 15"><rect x="1" y="1" width="18" height="13" fill="none" stroke="#fff" stroke-width="1.5"/><path d="M1 1l9 7 9-7" fill="none" stroke="#fff" stroke-width="1.5"/></svg>
<div class="abs foot-small" style="top:5110px;left:637px;color:#5d62e6">Mail Us</div>
<div class="abs foot-small" style="top:5124px;left:637px">info@brambleworth.com.au</div>

<div class="abs foot-head" style="top:4955px;left:818px">Our Newsletter</div>
<div class="abs foot-small" style="top:4990px;left:818px">Get the latest news &amp; updates</div>
<div class="abs" style="top:5017px;left:818px;width:200px;height:36px;border:1px solid #555;padding:11px 14px;font-size:8px;color:#bbb">Enter email...</div>
<div class="abs" style="top:5017px;left:1018px;width:42px;height:36px;background:var(--blue);display:flex;align-items:center;justify-content:center"><svg width="16" height="16" viewBox="0 0 16 16"><path d="M1 8l14-6-5 13-2-5z" fill="#fff"/></svg></div>

<div class="abs center copyright">©2022 Brambleworth Resources Pty Ltd. All rights reserved.</div>

</body>
</html>
```